Travel Blogger Business Card for wanderquill.net

I need a two-sided business card for a travel blogging website. The card should be both professional and fun at the same time. This is for the website www.wanderquill.net

I don't necessarily think that the current logo on the website needs to be used on the business card but it can be. I am very flexible with ideas

Target Market(s)

Travel agencies that will be met at a conference.

Industry/Entity Type

Travel

Contact Information for Business Card

Company Name: Wander Quill.net
Name: Marcel Vennor
Voice: +1-(345)-555-0193
Address: Coral Reed Shore, Grand Cayman, Cayman Islands
Email: ceo@wanderquill.net

Colors
0592cd
0355a3
3176b5
33a6d7
85cae6
85acd3

Requirements
Must have
• Website address and name should be bigger than address, phone number, and email.

```html
<!DOCTYPE html>
<html lang="en">
<head>
<meta charset="utf-8">
<title>Wander Quill.net – Business Card</title>
<link rel="stylesheet" href="https://fonts.googleapis.com/css2?family=Titillium+Web:wght@400;700&display=swap">
<style>
  :root {
    --brand-blue: #33a6d7;
    --deep-blue: #0592cd;
    --light-blue: #85cae6;
    --card-black: #1d1d1d;
    --paper: #ffffff;
    --stage: #e9ecef;
  }
  * { box-sizing: border-box; margin: 0; padding: 0; }
  html, body {
    width: 1200px; height: 950px; overflow: hidden;
    background: var(--stage);
    font-family: "Titillium Web", sans-serif;
  }
  .sheet { position: relative; width: 1200px; height: 950px; }
  .card {
    position: absolute; left: 250px; width: 700px; height: 400px;
    border-radius: 22px; overflow: hidden;
    box-shadow: 0 10px 28px rgba(0,0,0,.18);
  }
  .card--front { top: 50px; background: var(--paper); }
  .card--back { top: 500px; background: linear-gradient(135deg, #262626, var(--card-black)); }

  .front-panel { position: absolute; inset: 0; width: 700px; height: 400px; }

  .brand {
    position: absolute; display: flex; align-items: center; gap: 12px;
    font-weight: 400; font-size: 34px; letter-spacing: .5px;
    color: var(--brand-blue); white-space: nowrap;
  }
  .brand__dot {
    width: 20px; height: 20px; border-radius: 50%; background: var(--brand-blue); flex: none;
  }
  .card--front .brand { left: 40px; top: 226px; }

  .contact {
    position: absolute; right: 36px; top: 58px;
    color: var(--paper); text-align: right; line-height: 1.45;
  }
  .contact__name { font-weight: 700; font-size: 24px; margin-bottom: 6px; }
  .contact__line { font-size: 15px; display: flex; justify-content: flex-end; align-items: center; gap: 10px; }
  .contact__line--web { font-size: 17px; font-weight: 700; }
  .contact__icon { width: 16px; height: 16px; flex: none; }
  .contact__gap { height: 10px; }

  .back-art {
    position: absolute; right: 40px; top: 40px; width: 320px; height: 320px;
    border-radius: 50%;
    background: radial-gradient(circle at 50% 50%, var(--brand-blue) 0%, rgba(51,166,215,.55) 55%, rgba(51,166,215,0) 72%);
  }
  .card--back .brand { left: 56px; top: 160px; font-size: 44px; }
  .back-url {
    position: absolute; left: 88px; top: 222px;
    color: var(--paper); font-size: 18px; letter-spacing: 4px;
  }
</style>
</head>
<body>
<main class="sheet">

  <section class="card card--front" aria-label="Card front">
    <svg class="front-panel" viewBox="0 0 700 400" aria-hidden="true">
      <path d="M470,0 Q380,200 330,400 L700,400 L700,0 Z" fill="var(--brand-blue)"/>
    </svg>

    <div class="brand"><span class="brand__dot"></span>Wander Quill</div>

    <div class="contact">
      <p class="contact__name">Marcel Vennor</p>
      <p class="contact__line">Coral Reed Shore</p>
      <p class="contact__line">Grand Cayman</p>
      <p class="contact__line">Cayman Islands</p>
      <div class="contact__gap"></div>
      <p class="contact__line">+1-(345)-555-0193
        <svg class="contact__icon" viewBox="0 0 16 16" aria-hidden="true"><path d="M3 1.5l3 .5 1 3.5-2 1.2a9 9 0 004.3 4.3l1.2-2 3.5 1 .5 3-2 1.5C7 14 2 9 1.5 3.5z" fill="#fff"/></svg>
      </p>
      <p class="contact__line">ceo@wanderquill.net
        <svg class="contact__icon" viewBox="0 0 16 16" aria-hidden="true"><rect x="1" y="3" width="14" height="10" rx="1.5" fill="#fff"/><path d="M1.5 4l6.5 5 6.5-5" fill="none" stroke="var(--brand-blue)" stroke-width="1.4"/></svg>
      </p>
      <p class="contact__line contact__line--web">www.wanderquill.net
        <svg class="contact__icon" viewBox="0 0 16 16" aria-hidden="true"><circle cx="8" cy="8" r="7" fill="none" stroke="#fff" stroke-width="1.5"/><ellipse cx="8" cy="8" rx="3" ry="7" fill="none" stroke="#fff" stroke-width="1.2"/><path d="M1 8h14" stroke="#fff" stroke-width="1.2"/></svg>
      </p>
    </div>
  </section>

  <section class="card card--back" aria-label="Card back">
    <div class="back-art" role="img" aria-label="Large soft travel illustration in brand blue"></div>
    <div class="brand"><span class="brand__dot"></span>Wander Quill</div>
    <p class="back-url">wanderquill.net</p>
  </section>

</main>
</body>
</html>
```